Redesign our current website with a more professional feel

We currently have a running website that generates some traffic and looks ok but now we want to revamp it with professional eye catching design.
We are open to proposals and open to any new ideas or suggestions but we have to see your previous work.
our current site is www.brelk-solutions.com.au

Thank you for your time and we look forward to seeing your proposals

Target Market(s)

Business owners, managers

Industry/Entity Type

Security

Number of Pages Required

5+ page

```html
<!DOCTYPE html>
<html lang="en">
<head>
<meta charset="utf-8">
<title>Brelk Solutions – Security Company Sydney</title>
<link href="https://fonts.googleapis.com/css2?family=Questrial&family=Lato:wght@400;700&display=swap" rel="stylesheet">
<style>
:root{
  --navy:#1e3f8c;
  --navy-dark:#17306e;
  --blue-bar:#5b7cc4;
  --card-head:#234a9b;
  --grey-bg:#f1f1f1;
  --grey-pack:#6b6b6b;
  --text:#222;
  --muted:#555;
  --footer:#21478f;
  --copyright:#333;
  --white:#fff;
}
*{box-sizing:border-box;margin:0;padding:0}
html,body{width:679px;height:1200px;overflow:hidden;background:var(--white)}
body{position:relative;font-family:'Lato',sans-serif;color:var(--text)}
.abs{position:absolute}
.heading{font-family:'Questrial',sans-serif;font-weight:400}

.topbar{left:0;top:0;width:679px;height:22px;background:var(--blue-bar);color:var(--white);font-size:9.5px}
.topbar span{position:absolute;top:5px;display:flex;align-items:center;gap:4px}

.header{left:0;top:22px;width:679px;height:64px;background:var(--white)}
.brand{left:31px;top:24px;font-family:'Questrial',sans-serif;font-size:15px;color:var(--navy);letter-spacing:.3px;white-space:nowrap}
.nav{left:214px;top:26px;display:flex;align-items:center;font-family:'Questrial',sans-serif;font-size:10.5px;color:#222;letter-spacing:.4px}
.nav a{color:inherit;text-decoration:none;padding:0 9px;border-left:1px solid #999;line-height:11px}
.nav a.home{border:none;padding:0 8px 0 0}

.hero{left:0;top:86px;width:679px;height:232px;background:linear-gradient(90deg,#2a2d33 0%,#4a4f57 45%,#8d7766 75%,#b49a86 100%)}
.hero-title{left:50px;top:170px;font-family:'Questrial',sans-serif;font-size:19px;line-height:26px;color:var(--white)}
.hero-btn{left:77px;top:230px;width:182px;height:34px;border:2px solid #a9bdf0;background:var(--blue-bar);color:var(--white);font-family:'Questrial',sans-serif;font-size:14px;display:flex;align-items:center;justify-content:center}
.arrow{top:182px;width:20px;height:20px;background:#ddd;display:flex;align-items:center;justify-content:center}

.welcome-title{left:0;top:344px;width:679px;text-align:center;font-size:19px;color:var(--navy-dark)}
.rule{height:1px;background:#ccc}
.welcome-text{left:30px;top:384px;width:619px;text-align:center;font-size:8.3px;line-height:15.4px}
.btn{background:var(--navy-dark);color:var(--white);font-size:7.5px;display:flex;align-items:center;justify-content:center;border-radius:2px}

.services{left:0;top:504px;width:679px;height:210px;background:var(--grey-bg)}
.card{top:29px;width:148px;height:155px;background:var(--white)}
.card-head{height:26px;background:var(--card-head);color:var(--white);font-family:'Questrial',sans-serif;font-size:12px;display:flex;align-items:center;justify-content:center}
.card-img{position:absolute;left:7px;top:34px;width:134px;height:64px}
.card-text{position:absolute;left:6px;top:104px;width:136px;text-align:center;font-size:7.9px;line-height:12.8px}
.card-go{position:absolute;left:66px;top:148px}

.section-title{font-size:18px;color:var(--navy-dark)}
.pack{left:30px;width:180px;height:37px}
.pack-bar{position:absolute;left:26px;top:0;width:154px;height:36px;background:var(--grey-pack);color:var(--white);font-family:'Questrial',sans-serif;font-size:10.5px;line-height:15px;padding:3px 0 0 20px}
.pack-icon{position:absolute;left:0;top:-1px}

.news{left:239px;width:192px}
.date{position:absolute;left:0;top:0;width:27px;height:34px;text-align:center;font-family:'Questrial',sans-serif}
.date .d{background:#333;color:var(--white);font-size:11.5px;height:20px;line-height:20px}
.date .m{background:#ddd;color:#333;font-size:7px;height:14px;line-height:14px}
.news-body{position:absolute;left:35px;top:0;width:158px;font-size:7.3px;line-height:12.5px}

.promo{left:458px;top:736px;width:192px;height:123px;background:var(--navy);border-radius:3px;color:var(--white)}

.testimonials{left:0;top:892px;width:679px;height:168px;background:var(--grey-bg)}
.quote{left:144px;top:953px;width:506px;font-size:8.4px;line-height:15.2px;color:#222}

.footer{left:0;top:1060px;width:679px;height:118px;background:var(--footer);border-top:2px solid #4d72c4;color:var(--white)}
.f-head{font-family:'Questrial',sans-serif;font-size:10.5px}
.f-link{font-size:7.5px;color:#e3e9f7}
.f-small{font-size:7px;line-height:9px;color:#e3e9f7}
.copyright{left:0;top:1178px;width:679px;height:22px;background:var(--copyright);color:#ddd;font-size:7.2px;display:flex;align-items:center;justify-content:center}
</style>
</head>
<body>

<div class="abs topbar">
  <span style="left:433px">
    <svg width="11" height="8" viewBox="0 0 11 8"><rect x=".5" y=".5" width="10" height="7" fill="none" stroke="#fff"/><path d="M.5 .5 5.5 4.5 10.5 .5" fill="none" stroke="#fff"/></svg>
    info@brelk-solutions.com.au</span>
  <span style="left:575px">
    <svg width="10" height="10" viewBox="0 0 10 10"><circle cx="5" cy="5" r="4.3" fill="none" stroke="#fff"/><path d="M5 2.5V5l1.8 1.2" stroke="#fff" fill="none"/></svg>
    1300 22 4810</span>
</div>

<header class="abs header">
  <div class="abs brand">BRELK SOLUTIONS</div>
  <nav class="abs nav">
    <a class="home" href="#" aria-label="Home"><svg width="18" height="16" viewBox="0 0 18 16"><path d="M9 1 1 8h2.5v7h4v-4h3v4h4V8H17z" fill="#1e3f8c"/></svg></a>
    <a href="#">ABOUT US</a><a href="#">SERVICES</a><a href="#">SPECIAL OFFERS</a><a href="#">NEWS</a><a href="#">CONTACT US</a>
  </nav>
</header>

<div class="abs hero" role="img" aria-label="Security guard speaking into a handheld radio in a control room"></div>
<div class="abs hero-title">Quality Security Service By<br>Security Company Sydney</div>
<div class="abs hero-btn">GET STARTED WITH US</div>
<div class="abs arrow" style="left:0"><svg width="8" height="8" viewBox="0 0 8 8"><path d="M5.5 1 2.5 4l3 3" stroke="#333" stroke-width="1.6" fill="none"/></svg></div>
<div class="abs arrow" style="left:653px"><svg width="8" height="8" viewBox="0 0 8 8"><path d="M2.5 1 5.5 4l-3 3" stroke="#333" stroke-width="1.6" fill="none"/></svg></div>

<h1 class="abs heading welcome-title">WELCOME TO BRELK SOLUTIONS</h1>
<div class="abs rule" style="left:189px;top:378px;width:301px"></div>
<p class="abs welcome-text">Brelk Solutions is a corporate Security specialist committed to the provision of service to our customers. We provide a turnkey Security and event solution. The management team at Brelk Solutions offer our clients experience, in all facets of security work; ranging from static and mobile patrols through alarm response and tactical situations to surveillance, risk management and crowd/event control. We are an organisation with skills and experience to match the biggest in the industry. Our commitment to you – our client- is to provide only the best quality service, personnel and advice to meet your needs. All our personnel have undergone the most rigorous selection process and are fully trained, certified and capable.</p>
<div class="abs btn" style="left:313px;top:470px;width:53px;height:17px">Read More</div>

<section class="abs services">
  <div class="abs card" style="left:30px">
    <div class="card-head">Guarding</div>
    <div class="card-img" role="img" aria-label="Security guard in a suit holding a radio" style="background:linear-gradient(135deg,#3a3a3c,#8a8f96)"></div>
    <p class="card-text">Voluptatem Accusant Doloremque Laudan Aperiam, Eaque Ipsa Quae Ab Illo Volupt Accusant</p>
    <svg class="card-go" width="16" height="16" viewBox="0 0 16 16"><circle cx="8" cy="8" r="7.5" fill="#1e3f8c"/><path d="M7 5l3 3-3 3" stroke="#fff" stroke-width="1.5" fill="none"/></svg>
  </div>
  <div class="abs card" style="left:186px">
    <div class="card-head">Mobile Patrols</div>
    <div class="card-img" role="img" aria-label="Patrol cars lined up with officers in high-visibility vests" style="background:linear-gradient(180deg,#6f8a5e,#b7bcc0)"></div>
    <p class="card-text">Voluptatem Accusant Doloremque Laudan Aperiam, Eaque Ipsa Quae Ab Illo Volupt Accusant</p>
    <svg class="card-go" width="16" height="16" viewBox="0 0 16 16"><circle cx="8" cy="8" r="7.5" fill="#1e3f8c"/><path d="M7 5l3 3-3 3" stroke="#fff" stroke-width="1.5" fill="none"/></svg>
  </div>
  <div class="abs card" style="left:344px">
    <div class="card-head">Alarm Monitoring</div>
    <div class="card-img" role="img" aria-label="Operator watching a wall of monitoring screens" style="background:linear-gradient(135deg,#1d3f7a,#4c8ad0)"></div>
    <p class="card-text">Voluptatem Accusant Doloremque Laudan Aperiam, Eaque Ipsa Quae Ab Illo Volupt Accusant</p>
    <svg class="card-go" width="16" height="16" viewBox="0 0 16 16"><circle cx="8" cy="8" r="7.5" fill="#1e3f8c"/><path d="M7 5l3 3-3 3" stroke="#fff" stroke-width="1.5" fill="none"/></svg>
  </div>
  <div class="abs card" style="left:501px">
    <div class="card-head">CCTV &amp; Alarm Instlattion</div>
    <div class="card-img" role="img" aria-label="CCTV camera mounted on a brick wall" style="background:linear-gradient(135deg,#8e4a32,#c07a5c)"></div>
    <p class="card-text">Voluptatem Accusant Doloremque Laudan Aperiam, Eaque Ipsa Quae Ab Illo Volupt Accusant</p>
    <svg class="card-go" width="16" height="16" viewBox="0 0 16 16"><circle cx="8" cy="8" r="7.5" fill="#1e3f8c"/><path d="M7 5l3 3-3 3" stroke="#fff" stroke-width="1.5" fill="none"/></svg>
  </div>
</section>

<h2 class="abs heading section-title" style="left:30px;top:732px">Our Packages</h2>
<div class="abs rule" style="left:30px;top:760px;width:180px"></div>
<div class="abs pack" style="top:771px">
  <div class="pack-bar">Business Intruder Alarm<br>$40 Per Month Installed*</div>
  <svg class="pack-icon" width="38" height="38" viewBox="0 0 38 38"><circle cx="19" cy="19" r="18" fill="#1e3f8c" stroke="#fff" stroke-width="1.5"/><circle cx="19" cy="20" r="8" fill="none" stroke="#fff" stroke-width="2"/><path d="M19 15v5l3 2M11 12l3-2.5M27 12l-3-2.5" stroke="#fff" stroke-width="2" fill="none"/></svg>
</div>
<div class="abs pack" style="top:819px">
  <div class="pack-bar">CCTV Package<br>$80 Per Month Installed</div>
  <svg class="pack-icon" width="38" height="38" viewBox="0 0 38 38"><circle cx="19" cy="19" r="18" fill="#1e3f8c" stroke="#fff" stroke-width="1.5"/><path d="M10 13l16 4-2 5-15-4zM17 20l-2 5h-4v4" stroke="#fff" stroke-width="2" fill="none"/></svg>
</div>

<h2 class="abs heading section-title" style="left:239px;top:732px">Latest News</h2>
<svg class="abs" style="left:403px;top:739px" width="27" height="12" viewBox="0 0 27 12"><circle cx="6" cy="6" r="5" fill="none" stroke="#bbb"/><path d="M7 3.5 4.5 6 7 8.5" stroke="#bbb" fill="none"/><circle cx="20" cy="6" r="5" fill="none" stroke="#555"/><path d="M19 3.5 21.5 6 19 8.5" stroke="#555" fill="none"/></svg>
<div class="abs rule" style="left:239px;top:760px;width:192px"></div>
<div class="abs news" style="top:772px;height:34px">
  <div class="date"><div class="d">07</div><div class="m">JAN</div></div>
  <div class="news-body"><b>Sed ut perspiciatis unde omnis iste</b><br>Voluptatem Accusant Doloremque Laudan Aperiam, Eaque Ipsa Quae Ab Illo.</div>
</div>
<div class="abs rule" style="left:239px;top:813px;width:192px;background:#e2e2e2"></div>
<div class="abs news" style="top:822px;height:34px">
  <div class="date"><div class="d">07</div><div class="m">JAN</div></div>
  <div class="news-body"><b>Sed ut perspiciatis unde omnis iste</b><br>Voluptatem Accusant Doloremque Laudan Aperiam, Eaque Ipsa Quae Ab Illo.</div>
</div>

<aside class="abs promo">
  <svg class="abs" style="left:8px;top:9px" width="38" height="38" viewBox="0 0 38 38"><circle cx="19" cy="19" r="17" fill="#4d6fb8"/><text x="19" y="25" text-anchor="middle" font-family="Questrial,sans-serif" font-size="18" fill="#1e3f8c">%</text></svg>
  <div class="abs heading" style="left:53px;top:16px;font-size:19px">3 Months FREE</div>
  <div class="abs" style="left:0;top:56px;width:192px;text-align:center;font-family:'Questrial',sans-serif;font-size:10px;line-height:15.5px">Back To Base Alarm Monitoring<br>With All New Installations</div>
  <div class="abs btn" style="left:71px;top:94px;width:52px;height:18px;background:#5b7cc4">Learn More</div>
</aside>

<section class="abs testimonials"></section>
<h2 class="abs heading section-title" style="left:0;top:907px;width:679px;text-align:center">Clients Testimonials</h2>
<div class="abs rule" style="left:218px;top:938px;width:215px"></div>
<svg class="abs" style="left:38px;top:946px" width="82" height="84" viewBox="0 0 82 84"><path d="M60 72l0 12-12-7z" fill="#1e3f8c"/><circle cx="40" cy="40" r="39" fill="#1e3f8c"/></svg>
<div class="abs" role="img" aria-label="Client portrait" style="left:42px;top:950px;width:72px;height:72px;border-radius:50%;background:linear-gradient(160deg,#d8dde4,#9aa3ad)"></div>
<svg class="abs" style="left:140px;top:948px" width="22" height="16" viewBox="0 0 22 16"><path d="M9 2C4 3 1 6 1 10a4 4 0 1 0 4-4c0-1 1-2 4-3zM21 2c-5 1-8 4-8 8a4 4 0 1 0 4-4c0-1 1-2 4-3z" fill="#c8c8c8"/></svg>
<p class="abs quote"><span style="padding-left:21px"></span>Lorem ipsum dolor smit amet, consectetuer adipiscing elitmk, sed amet diam nonummy nibh euismod tincidun nt ut laoreetml dolore magna aliquam erat volutpat. Ut wisi enim ad minim veniam, quis nostrud exer tationk ullamcorper suscipit lobortisk nisl utml aliqpi ex ea commodo consequat. Duis autem vel eumk iriure dolor inj hendrerit inn vulputate velit esse molestiemo consequat, velhki illumn gnol dolore eu feugiat nulla facilisis .</p>
<div class="abs rule" style="left:141px;top:1020px;width:509px"></div>
<div class="abs" style="left:144px;top:1026px;font-size:10.5px;font-weight:700;color:var(--navy);letter-spacing:.4px">- Mr. Sam Porter</div>
<svg class="abs" style="left:623px;top:1027px" width="27" height="8" viewBox="0 0 27 8"><circle cx="4" cy="4" r="3" fill="none" stroke="#555"/><circle cx="4" cy="4" r="1.3" fill="#555"/><circle cx="13" cy="4" r="3" fill="#bbb"/><circle cx="22" cy="4" r="3" fill="#bbb"/></svg>

<footer class="abs footer">
  <div class="abs f-head" style="left:31px;top:13px">Quick Links</div>
  <div class="abs rule" style="left:31px;top:30px;width:106px;background:#5577bb"></div>
  <div class="abs f-link" style="left:36px;top:40px;line-height:19.2px">› &nbsp;Home<br>› &nbsp;About Us<br>› &nbsp;Services<br>› &nbsp;Special</div>
  <div class="abs f-link" style="left:93px;top:40px;line-height:19.2px">› &nbsp;Offers<br>› &nbsp;News<br>› &nbsp;Contact Us</div>
  <div class="abs rule" style="left:154px;top:15px;width:1px;height:90px;background:#3d61a8"></div>

  <div class="abs f-head" style="left:174px;top:13px">Contact Details</div>
  <div class="abs rule" style="left:174px;top:30px;width:130px;background:#5577bb"></div>
  <svg class="abs" style="left:175px;top:41px" width="7" height="10" viewBox="0 0 7 10"><path d="M3.5 0A3.5 3.5 0 0 0 0 3.5C0 6 3.5 10 3.5 10S7 6 7 3.5A3.5 3.5 0 0 0 3.5 0z" fill="#fff"/><circle cx="3.5" cy="3.5" r="1.3" fill="#21478f"/></svg>
  <div class="abs f-small" style="left:189px;top:40px;width:120px">Lorem ipsum dolor consectetuer adipiscing elit, sed diam nonummy bitasa street:395001</div>
  <svg class="abs" style="left:174px;top:75px" width="9" height="9" viewBox="0 0 9 9"><path d="M1.5 0 3.5 2.5 2.5 3.8C3.2 5.2 4 6 5.3 6.6L6.5 5.5 9 7.5 8 9C4 9 0 5 0 1z" fill="#fff"/></svg>
  <div class="abs f-small" style="left:189px;top:75px">1300 22 4810</div>
  <svg class="abs" style="left:174px;top:95px" width="9" height="7" viewBox="0 0 9 7"><rect width="9" height="7" fill="#fff"/><path d="M0 0l4.5 3.5L9 0" stroke="#21478f" fill="none"/></svg>
  <div class="abs f-small" style="left:189px;top:94px">info@brelk-solutions.com.au</div>
  <div class="abs rule" style="left:327px;top:15px;width:1px;height:90px;background:#3d61a8"></div>

  <div class="abs f-head" style="left:346px;top:13px">Subscribe to Newsletter</div>
  <div class="abs rule" style="left:346px;top:30px;width:123px;background:#5577bb"></div>
  <div class="abs f-small" style="left:347px;top:40px;width:130px;line-height:12px">Lorem ipsudolor sit coec adipiscing elitsite amet</div>
  <div class="abs" style="left:347px;top:66px;width:118px;height:15px;background:#fff;color:#777;font-size:6.5px;padding:4px 0 0 5px">Email Address</div>
  <div class="abs" style="left:347px;top:86px;width:60px;height:16px;background:#5b7cc4;font-size:8px;font-weight:700;display:flex;align-items:center;justify-content:center">SUBSCRIBE</div>
  <div class="abs rule" style="left:495px;top:15px;width:1px;height:90px;background:#3d61a8"></div>

  <div class="abs" style="left:522px;top:30px;width:112px;text-align:center;font-family:'Questrial',sans-serif;font-size:20px;color:#6f8fcf;letter-spacing:1px">BRELK</div>
  <svg class="abs" style="left:544px;top:83px" width="68" height="18" viewBox="0 0 68 18"><circle cx="9" cy="9" r="8" fill="#3a3a3a"/><circle cx="33" cy="9" r="8" fill="#4a90e2"/><circle cx="57" cy="9" r="8" fill="#3a3a3a"/></svg>
</footer>
<div class="abs copyright">Copyright © 2016 - BRELK Solutions. All Rights Reserved.</div>

</body>
</html>
```